Vial Crate Guild - A Monthly Subscription for Essential Oils - Shopify Website Design

A monthly subscription company. Need a Shopify Website Design and uploaded to fully work with Tidy Renewals.

Please look at these sites for examples as well as the images I enclosed.

https://purelymeadow.example/
https://www.bloomup-ax.example/
https://www.dinnerkitly.example/
https://www.globalsnackos.example/

Number of Pages Required

1 page

```html
<!DOCTYPE html>
<html lang="en">
<head>
<meta charset="utf-8">
<title>Vial Crate Guild</title>
<link rel="stylesheet" href="https://fonts.googleapis.com/css2?family=Roboto+Condensed:wght@700&family=Lato:wght@400;700&display=swap">
<style>
:root{
  --ink:#111;
  --text:#444;
  --muted:#666;
  --accent:#f07f6a;
  --footer:#fdf3f1;
  --white:#fff;
}
*{margin:0;padding:0;box-sizing:border-box}
html,body{width:1200px;height:3101px;overflow:hidden}
body{position:relative;background:var(--white);font-family:'Lato',sans-serif;color:var(--text)}
.abs{position:absolute}
.heading{font-family:'Roboto Condensed',sans-serif;font-weight:700;color:var(--ink);text-transform:uppercase}
.center{left:0;width:1200px;text-align:center}

.topbar{top:0;left:0;width:1200px;height:35px;background:var(--ink);color:var(--white);font-size:11px;font-weight:700;text-align:center;line-height:35px}
.topbar svg{position:absolute;right:150px;top:12px}

.brand{display:flex;align-items:center;gap:10px;font-family:'Lato',sans-serif;font-weight:700;color:var(--ink);font-size:22px;white-space:nowrap}
.brand .mark{width:14px;height:14px;background:var(--accent)}
.site-brand{left:144px;top:59px;height:32px}
.footer-brand{left:0;width:1200px;justify-content:center;top:2674px;height:32px}
.nav{top:67px;font-size:13px;color:var(--ink);display:flex;gap:30px;right:145px}

.hero{top:116px;left:0;width:1200px;height:485px;background:linear-gradient(100deg,#5a3a24 0%,#7a5636 35%,#9b8a6a 60%,#d9d6c4 80%,#e6e3d6 100%)}
.hero-card{left:390px;top:195px;width:396px;height:247px;background:var(--white);text-align:center}
.hero-card h1{font-size:46px;line-height:64px;margin-top:34px;white-space:nowrap}
.hero-card p{font-size:15px;line-height:22px;color:var(--text);margin:22px 40px 0}
.hero-card .cta{font-size:15px;color:var(--text);margin-top:22px;display:inline-flex;align-items:center;gap:10px}

.section-title{font-size:25px}
.rule{width:40px;height:2px;background:var(--accent);left:580px}

.intro{top:758px;left:206px;width:788px;text-align:center;font-size:14px;line-height:25px;color:var(--text)}

.product-img{top:976px;width:285px;height:278px}
.product-name{top:1282px;width:285px;text-align:center;font-size:16px;font-weight:700;color:var(--ink)}

.popular{top:1383px;left:0;width:1200px;height:432px;background:linear-gradient(100deg,#3b2a20 0%,#5c3e2a 40%,#6b4630 60%,#3e5a58 100%)}
.popular-label{left:412px;top:1566px;width:376px;height:66px;background:var(--white);font-size:38px;line-height:66px;text-align:center}

.news{top:1984px;width:433px;height:367px}
.news-title{left:37px;bottom:33px;font-family:'Lato',sans-serif;font-weight:700;color:var(--white);font-size:22px;line-height:30px;text-transform:uppercase}

.feature{top:2425px;width:300px;text-align:center}
.feature h3{font-size:16px;font-weight:700;color:var(--ink);margin-top:20px;font-family:'Lato',sans-serif}
.feature p{font-size:12px;color:var(--muted);margin-top:13px}

.footer{top:2625px;left:0;width:1200px;height:476px;background:var(--footer)}
.col-title{top:2774px;font-size:16px;font-weight:700;color:var(--ink);font-family:'Lato',sans-serif}
.menu{top:2810px;left:143px;list-style:none;font-size:12px;line-height:26.5px;color:var(--muted)}
.about{top:2810px;left:311px;width:380px;font-size:12px;line-height:22px;color:var(--muted)}
.news-copy{top:2810px;left:757px;width:290px;font-size:12px;line-height:22px;color:var(--muted)}
.signup{top:2875px;left:757px;width:299px;height:40px;display:flex}
.signup .field{flex:1;border:1px solid #ccc;background:var(--white);font-size:10px;color:var(--ink);padding:0 18px;line-height:38px}
.signup .join{width:74px;background:var(--ink);color:var(--white);font-size:16px;font-weight:700;text-align:center;line-height:40px}
.copyright{top:2993px;font-size:12px;color:var(--muted)}
.payments{top:3047px;left:495px;width:210px;display:flex;justify-content:space-between}
.payments span{width:26px;height:16px;border-radius:3px}
</style>
</head>
<body>
<div class="abs topbar">FREE SHIPPING ON ORDERS OVER $100
  <svg width="11" height="11" viewBox="0 0 11 11"><circle cx="4.5" cy="4.5" r="3.3" fill="none" stroke="#fff" stroke-width="1.8"/><line x1="7" y1="7" x2="10" y2="10" stroke="#fff" stroke-width="2"/></svg>
</div>

<div class="abs brand site-brand"><span class="mark"></span>Vial Crate Guild</div>
<nav class="abs nav"><span>HOME</span><span>SHOP</span><span>BLOG</span><span>CONTACT</span><span>ABOUT US</span></nav>

<div class="abs hero" role="img" aria-label="Wooden drawer with a towel and an amber essential oil bottle beside dried lavender"></div>
<div class="abs hero-card">
  <h1 class="heading">Vial Crate Guild</h1>
  <p>Sed ut perspiciatis unde omnis iste natus error sit voluptatem accusantium</p>
  <span class="cta">Shop Now
    <svg width="16" height="8" viewBox="0 0 16 8"><line x1="0" y1="4" x2="13" y2="4" stroke="#222" stroke-width="2"/><path d="M10 0 L16 4 L10 8Z" fill="#222"/></svg>
  </span>
</div>
<svg class="abs" style="left:587px;top:546px" width="26" height="16" viewBox="0 0 26 16"><polyline points="2,2 13,13 24,2" fill="none" stroke="#fff" stroke-width="3"/></svg>

<h2 class="abs center heading section-title" style="top:675px">Welcome to Vial Crate Guild</h2>
<div class="abs rule" style="top:716px"></div>
<p class="abs intro">Lorem ipsum dolor sit amet, consectetur adipiscing elit, sed do eiusmod tempor incididunt ut labore et dolore magna aliqua.is ipsum suspendisse ultrices gravidas commodo viverra maecenas accumsan lacus vel facpsum dolor sit ameadipiscing elitsed do eiusmod tempor incididunt labore et dolore magna aliqua.ismmodo viverra maecenas accumsan lacus vel facilisis.</p>

<h2 class="abs center heading section-title" style="top:884px">Featured Products</h2>
<div class="abs rule" style="top:926px"></div>

<div class="abs product-img" style="left:144px;background:linear-gradient(160deg,#dcdcdc,#c9c9c9)" role="img" aria-label="Open wooden box holding rows of essential oil bottles"></div>
<div class="abs product-img" style="left:457px;background:linear-gradient(90deg,#e6e6e6,#cfcfcf 45%,#e8e8e8)" role="img" aria-label="White gift box with a single gold-capped oil vial"></div>
<div class="abs product-img" style="left:770px;background:linear-gradient(160deg,#d4d4d4,#efefef)" role="img" aria-label="White carton holding four dropper bottles"></div>
<div class="abs product-name" style="left:144px">PRODUCT NAME</div>
<div class="abs product-name" style="left:457px">PRODUCT NAME</div>
<div class="abs product-name" style="left:770px">PRODUCT NAME</div>

<div class="abs popular" role="img" aria-label="Rustic wooden crate of dark oil bottles beside an orchid on driftwood"></div>
<div class="abs heading popular-label">Popular Products</div>
<svg class="abs" style="left:76px;top:1583px" width="22" height="34" viewBox="0 0 22 34"><polyline points="19,2 4,17 19,32" fill="none" stroke="#fff" stroke-width="4"/></svg>
<svg class="abs" style="left:1101px;top:1583px" width="22" height="34" viewBox="0 0 22 34"><polyline points="3,2 18,17 3,32" fill="none" stroke="#fff" stroke-width="4"/></svg>

<h2 class="abs center heading section-title" style="top:1893px">Recent News</h2>
<div class="abs rule" style="top:1934px"></div>

<div class="abs news" style="left:156px;background:linear-gradient(180deg,#d8d8d8 0%,#8a8a8a 45%,#1a1a1a 75%,#000 100%)" role="img" aria-label="Open white box revealing an oil vial">
  <div class="abs news-title">Lorem ipsum dolor sit<br>amet consectetur</div>
</div>
<div class="abs news" style="left:611px;background:linear-gradient(180deg,#7a5a40 0%,#4a3a2c 45%,#1a1410 75%,#000 100%)" role="img" aria-label="Wooden tray of compartments filled with oil bottles">
  <div class="abs news-title">Lorem ipsum dolor sit<br>amet consectetur</div>
</div>

<div class="abs feature" style="left:122px">
  <svg width="34" height="34" viewBox="0 0 34 34"><path d="M6 15 A11 11 0 0 1 27 11" fill="none" stroke="#f07f6a" stroke-width="5"/><path d="M23 5 L31 12 L21 15Z" fill="#f07f6a"/><path d="M28 19 A11 11 0 0 1 7 23" fill="none" stroke="#f07f6a" stroke-width="5"/><path d="M11 29 L3 22 L13 19Z" fill="#f07f6a"/></svg>
  <h3>FREE RETURNS</h3><p>Returns within 30 days receive a full refund.</p>
</div>
<div class="abs feature" style="left:461px">
  <svg width="34" height="34" viewBox="0 0 34 34"><circle cx="17" cy="17" r="15" fill="#f07f6a"/><path d="M9 9 Q14 12 12 17 Q16 20 14 26 Q8 22 7 15Z M20 6 Q25 10 22 14 Q27 17 27 22 Q22 20 19 16Z" fill="#fff"/></svg>
  <h3>WORDWIDE SHIPPING</h3><p>Ship anywhere, rates available at checkout.</p>
</div>
<div class="abs feature" style="left:806px">
  <svg width="34" height="34" viewBox="0 0 34 34"><path d="M5 22 V17 A12 12 0 0 1 29 17 V22" fill="none" stroke="#f07f6a" stroke-width="4"/><rect x="4" y="18" width="7" height="11" rx="2" fill="#f07f6a"/><rect x="23" y="18" width="7" height="11" rx="2" fill="#f07f6a"/></svg>
  <h3>24/7 SUPPORT</h3><p>Call us anytime at 1(55) 55-0100</p>
</div>

<div class="abs footer"></div>
<div class="abs brand footer-brand"><span class="mark"></span>Vial Crate Guild</div>

<h4 class="abs col-title" style="left:143px">MAIN MENU</h4>
<ul class="abs menu"><li>Home</li><li>Shop</li><li>Blog</li><li>About</li><li>Contact</li></ul>

<h4 class="abs col-title" style="left:311px">ABOUT US</h4>
<p class="abs about">Lorem ipsum dolor sit amet, consectetur adipiscing elit, sed do eiusmod tempor incididunt ut labore et dolore magna aliquais ipsum suspendisse ultrices gravida. Risus commodo viverra maecenas accumsan lacus vel facilisis. Lorem ipsum dolor sit amet, consectetur adipiscing elit, sed do eiusmod tempor incididunt ut labore et dolore magna</p>

<h4 class="abs col-title" style="left:757px">NEWSLETTER</h4>
<p class="abs news-copy">Subscribe to get special offers, free giveaways, and once-in-a-lifetime deals.</p>
<div class="abs signup"><div class="field">Enter Email</div><div class="join">JOIN</div></div>

<p class="abs center copyright">© 2020 Vial Crate Guild.All Rights Reserved &nbsp;|&nbsp; Privacy Policy &nbsp;|&nbsp; Terms and use</p>
<div class="abs payments">
  <span style="background:#dfe3ee"></span>
  <span style="background:#f3c1b0"></span>
  <span style="background:#4a7bc0"></span>
  <span style="background:#d6e0f0"></span>
  <span style="background:#cfe2f3"></span>
  <span style="background:#f4e2c8"></span>
</div>
</body>
</html>
```